Gleamstone Works website

Epoxy Resin Flooring for home renovations and commercial property.
3 page website homepage, contact us and gallery with a link to Snapvelle.
Looking for someone to create a visually pleasing website for home transformation and design. I have attached some designs of completed work however I can send you many more. Use colour and don’t inspiration from the logo. If happy with stage one we will add a commercial page as a new project.

Target Market(s)

Homeowners that want to improve their home or rental property

Industry/Entity Type

Home improvements

Coding

Coded - Design and coding required

Number of Pages Required

3 page

Requirements
Must have
• Home Page, Contact Us page and showcase / gallery page
Nice to have
• I would like the colour theme to be taken from the logo, a clean finish with artistic usuals to get homeowners excited about their project

```html
<!DOCTYPE html>
<html lang="en">
<head>
<meta charset="utf-8">
<title>Gleamstone Works – Epoxy Resin Flooring</title>
<link href="https://fonts.googleapis.com/css2?family=Poppins:ital,wght@0,400;0,500;0,600;0,700;1,400&display=swap" rel="stylesheet">
<style>
:root{
  --red:#ec1c24;
  --red-soft:#f0464c;
  --pink:#fdeaec;
  --ink:#111111;
  --grey:#555;
  --white:#ffffff;
  --black:#0b0b0b;
}
*{box-sizing:border-box;margin:0;padding:0}
html,body{width:1200px;height:3755px;overflow:hidden;background:var(--white);font-family:'Poppins',sans-serif;color:var(--ink)}
.page{position:relative;width:1200px;height:3755px;overflow:hidden}
.abs{position:absolute}
.btn{position:absolute;display:flex;align-items:center;justify-content:center;background:var(--red);color:var(--white);border-radius:30px;font-size:13px;font-weight:500}
.section-title{position:absolute;left:0;width:1200px;text-align:center;font-size:33px;font-weight:700}
/* header */
.brand{position:absolute;left:140px;top:24px;font-size:26px;font-weight:700;color:var(--ink);letter-spacing:.5px}
.brand-sub{position:absolute;left:140px;top:58px;width:164px;font-size:11px;font-weight:600;color:var(--red);letter-spacing:2px}
.nav a{position:absolute;top:42px;font-size:12px;color:var(--ink);text-decoration:none}
.nav a.active{font-weight:600;border-bottom:1.5px solid var(--ink)}
/* hero */
.hero-photo{left:0;top:100px;width:1200px;height:530px;background:linear-gradient(90deg,#1c1f22 0%,#33383b 45%,#5a5e62 100%)}
.hero-right{left:0;top:100px;width:1200px;height:575px}
.hero h1{position:absolute;left:140px;top:248px;width:480px;font-size:33px;line-height:47px;color:var(--white);font-weight:700}
.hero p{position:absolute;left:142px;top:358px;width:420px;font-size:15px;line-height:29px;color:var(--white)}
/* services */
.card{position:absolute;top:840px;width:222px;height:305px;border-radius:16px;background:var(--pink);overflow:hidden}
.card .img{height:144px}
.card h3{margin:22px 0 0 28px;font-size:16px;font-weight:600}
.card p{margin:6px 20px 0 28px;font-size:11px;line-height:18.5px;color:#333}
.card a{display:block;margin:6px 0 0 28px;font-size:11px;font-weight:600;color:var(--red);text-decoration:underline}
.card.featured{background:var(--red)}
.card.featured h3,.card.featured p,.card.featured a{color:var(--white)}
/* features */
.features{left:0;top:1325px;width:1200px;height:517px;background:linear-gradient(90deg,#e5232b,#f2343c 60%,#ee2c35)}
.feat h4{font-size:15px;font-weight:500;color:var(--white)}
.feat p{font-size:10px;line-height:16px;color:var(--white)}
.emblem{left:535px;top:300px;width:130px;height:130px;border-radius:50%;background:radial-gradient(circle,rgba(255,255,255,.45),rgba(255,255,255,.08) 70%,rgba(255,255,255,0))}
/* testimonial */
.quote{position:absolute;left:528px;top:2078px;width:478px;font-size:15px;line-height:24px;font-style:italic;color:#333;text-align:justify}
/* gallery */
.tile{position:absolute;width:229px;height:230px}
/* contact */
.field{position:absolute;background:var(--white);border-radius:12px;font-size:11px;color:#444;padding:10px 15px}
/* footer */
.footer-nav a{position:absolute;top:3528px;font-size:13px;color:var(--white);text-decoration:none}
.info{position:absolute;top:3618px;font-size:13px;line-height:22px;color:var(--white)}
</style>
</head>
<body>
<div class="page">

  <header>
    <div class="brand">GLEAMSTONE</div>
    <div class="brand-sub">WORKS</div>
    <nav class="nav">
      <a class="active" style="left:559px">Home</a>
      <a style="left:635px">Services</a>
      <a style="left:725px">Gallery</a>
      <a style="left:807px">Contact</a>
    </nav>
    <div class="btn" style="left:884px;top:30px;width:174px;height:40px;font-size:12px">Get A Free Estimate</div>
  </header>

  <section class="hero">
    <div class="abs hero-photo" role="img" aria-label="Dark room interior with plants and a grey epoxy floor"></div>
    <svg class="abs hero-right" width="1200" height="575" viewBox="0 0 1200 575">
      <polygon points="872,0 1200,0 1200,530 1160,575 593,575" fill="#b9bec3" role="img" aria-label="Hallway with window and speckled grey epoxy floor"/>
      <polygon points="862,0 872,0 609,575 593,575" fill="#ec1c24"/>
      <polygon points="1155,0 1200,0 1200,20 990,530 1000,575 948,575" fill="#ffffff"/>
      <rect x="0" y="530" width="600" height="45" fill="#ffffff"/>
      <rect x="980" y="530" width="220" height="45" fill="#ffffff"/>
      <g stroke="#d9d9d9" stroke-width="1.5">
        <line x1="0" y1="547" x2="600" y2="547"/><line x1="0" y1="560" x2="600" y2="560"/><line x1="0" y1="571" x2="600" y2="571"/>
        <line x1="980" y1="543" x2="1200" y2="543"/><line x1="980" y1="555" x2="1200" y2="555"/>
      </g>
      <circle cx="895" cy="287" r="36" fill="#7b1d21" opacity=".55"/>
      <circle cx="895" cy="287" r="26" fill="#ec1c24"/>
      <polygon points="887,275 907,287 887,299" fill="#fff"/>
      <circle cx="150" cy="458" r="5" fill="#cfcfcf"/>
      <circle cx="181" cy="458" r="9" fill="none" stroke="#ec1c24" stroke-width="2"/>
      <circle cx="181" cy="458" r="5" fill="#ec1c24"/>
      <circle cx="212" cy="458" r="5" fill="#cfcfcf"/>
      <circle cx="243" cy="458" r="5" fill="#cfcfcf"/>
    </svg>
    <h1>Transform Your Home with Epoxy Resin Flooring</h1>
    <p>Expert solutions for homeowners looking to improve their property</p>
    <div class="btn" style="left:142px;top:431px;width:132px;height:40px">Get a Quote</div>
  </section>

  <section>
    <h2 class="section-title" style="top:752px">Our Services</h2>
    <div class="card" style="left:140px"><div class="img" role="img" aria-label="Residential apartment buildings" style="background:linear-gradient(#4e8ad0,#c9c2b4 70%,#5e8a4a)"></div><h3>Residential</h3><p>Lorem ipsum dolor sit amet, consectetur adipiscing elit, sed odo viverra maecenas ac</p><a>Read More</a></div>
    <div class="card" style="left:373px"><div class="img" role="img" aria-label="Modern glass commercial building" style="background:linear-gradient(#8cc0ea,#4a6b80 65%,#6d9a5a)"></div><h3>Commercial</h3><p>Lorem ipsum dolor sit amet, consectetur adipiscing elit, sed odo viverra maecenas ac</p><a>Read More</a></div>
    <div class="card featured" style="left:605px"><div class="img" role="img" aria-label="Worker installing floor tiles" style="background:linear-gradient(#7d7874,#5b5a5a)"></div><h3>Installation</h3><p>Lorem ipsum dolor sit amet, consectetur adipiscing elit, sed odo viverra maecenas ac</p><a>Read More</a></div>
    <div class="card" style="left:837px"><div class="img" role="img" aria-label="Worker repairing a roof" style="background:linear-gradient(120deg,#b9c6d0,#6c5a50 60%,#3c3c40)"></div><h3>Repairs</h3><p>Lorem ipsum dolor sit amet, consectetur adipiscing elit, sed odo viverra maecenas ac</p><a>Read More</a></div>
    <div class="btn" style="left:535px;top:1197px;width:130px;height:42px">Contact Us</div>
  </section>

  <section class="abs features" role="img" aria-label="Red tinted living room backdrop">
    <h2 class="section-title" style="top:62px;color:#fff">Our Features</h2>
    <svg class="abs" style="left:0;top:0" width="1200" height="517" viewBox="0 0 1200 517">
      <g fill="none" stroke="#ffffff" stroke-opacity=".7" stroke-dasharray="2 4">
        <path d="M390 310 Q430 200 497 203"/>
        <path d="M497 203 Q600 170 690 203"/>
        <path d="M690 203 Q780 230 808 330"/>
      </g>
      <path d="M458 398 A142 142 0 0 1 742 398" fill="none" stroke="#fff" stroke-width="16"/>
      <g fill="none" stroke="#fff" stroke-width="2">
        <circle cx="497" cy="203" r="29"/><circle cx="690" cy="203" r="29"/>
        <circle cx="390" cy="340" r="29"/><circle cx="808" cy="340" r="29"/>
      </g>
      <g fill="none" stroke="#fff" stroke-width="1.8">
        <circle cx="497" cy="203" r="10"/><path d="M490 196 L504 210"/>
        <circle cx="683" cy="200" r="7"/><circle cx="695" cy="208" r="7"/>
        <path d="M377 348 L390 334 L403 348 M381 345 V356 H399 V345"/>
        <circle cx="808" cy="332" r="4"/><path d="M808 336 V350 M800 342 H816 M802 358 L808 350 L814 358"/>
      </g>
    </svg>
    <div class="abs emblem" role="img" aria-label="Resin drop emblem"></div>
    <div class="abs feat" style="left:240px;top:162px;width:194px;text-align:right"><h4>Custom Designs</h4><p>Lorem ipsum dolor sit amet, consectetur adipiscing elit, sed do</p></div>
    <div class="abs feat" style="left:751px;top:162px;width:220px"><h4>Durable and Long-Lasting</h4><p>Lorem ipsum dolor sit amet, consectetur adipiscing elit, sed do</p></div>
    <div class="abs feat" style="left:150px;top:316px;width:190px;text-align:right"><h4>Professional Installation</h4><p>Lorem ipsum dolor sit amet, consectetur adipiscing elit, sed do</p></div>
    <div class="abs feat" style="left:860px;top:316px;width:200px"><h4>Wide Range of Colors and Finishes</h4><p>Lorem ipsum dolor sit amet, consectetur adipiscing elit, sed do</p></div>
  </section>

  <section>
    <h2 class="section-title" style="top:1915px">Testimonials</h2>
    <svg class="abs" style="left:0;top:1990px" width="1200" height="310" viewBox="0 0 1200 310">
      <line x1="0" y1="168" x2="95" y2="168" stroke="#999"/>
      <line x1="1110" y1="168" x2="1200" y2="168" stroke="#999"/>
      <circle cx="115" cy="168" r="21" fill="#fff" stroke="#f4c1c3" stroke-width="2"/>
      <path d="M119 160 L111 168 L119 176" fill="none" stroke="#f4a0a4" stroke-width="2"/>
      <circle cx="1087" cy="168" r="21" fill="#ec1c24"/>
      <path d="M1083 160 L1091 168 L1083 176" fill="none" stroke="#fff" stroke-width="2.5"/>
      <circle cx="245" cy="70" r="58" fill="#f0464c"/>
      <circle cx="445" cy="262" r="40" fill="none" stroke="#f6d2d4" stroke-width="2"/>
      <circle cx="348" cy="160" r="138" fill="#f0464c"/>
      <circle cx="348" cy="160" r="128" fill="#c9b6ac" role="img" aria-label="Portrait of a construction worker in a hard hat"/>
    </svg>
    <div class="abs" style="left:530px;top:2060px;font-size:44px;color:#ddd;font-family:Georgia,serif">&#8220;</div>
    <p class="quote">&#8195;&#8195;Lorem ipsum dolor sit amet, consectetuer adipiscing elit, sed diam nonummy nibh euismod tincidunt ut laoreet dolore magna aliquam erat volutpat. Ut wisi enim ad minim veniam, quis nostrud exerci tation ullamcorper suscipit lobortis nisl ut aliquip ex ea commodo consequat. Duis autem vel eum iriure dolor in hendrerit in vulputate velit esse molestie consequat.</p>
    <div class="abs" style="left:920px;top:2188px;font-size:44px;color:#ddd;font-family:Georgia,serif">&#8221;</div>
  </section>

  <section>
    <h2 class="section-title" style="top:2370px">Our Gallery</h2>
    <div class="tile" style="left:0;top:2457px;background:linear-gradient(#5c6a5e,#2d2a26 60%,#c9c9c9)" role="img" aria-label="Kitchen island with glossy floor"></div>
    <div class="tile" style="left:243px;top:2457px;background:linear-gradient(#e5e1db,#7b7570 60%,#d8d6d2)" role="img" aria-label="Living room with lounge chair"></div>
    <div class="tile" style="left:486px;top:2457px;background:linear-gradient(#f1ede6,#a98a6c 55%,#e9e5de)" role="img" aria-label="Hallway with marble floor"></div>
    <div class="tile" style="left:728px;top:2457px;background:linear-gradient(#6a5d52,#e0ddd6 55%,#cfcac2)" role="img" aria-label="Lobby with elevators"></div>
    <div class="tile" style="left:971px;top:2457px;background:linear-gradient(#eceae5,#8a7766 60%,#595551)" role="img" aria-label="Open plan living area"></div>
    <div class="tile" style="left:0;top:2700px;background:linear-gradient(#ecebe8,#c8c4bd 70%,#a39d96)" role="img" aria-label="White marble feature wall"></div>
    <div class="tile" style="left:243px;top:2700px;background:linear-gradient(90deg,#1d1d1f,#3b3b3d 40%,#e8e6e3)" role="img" aria-label="Glass partition with console table"></div>
    <div class="tile" style="left:486px;top:2700px;background:linear-gradient(#f2efea,#b8a08a 55%,#f3f1ee)" role="img" aria-label="Bright bathroom vanity"></div>
    <div class="tile" style="left:728px;top:2700px;background:linear-gradient(#d9d8d6,#3b4044 50%,#bfbdb8)" role="img" aria-label="Large room with polished floor"></div>
    <div class="tile" style="left:971px;top:2700px;background:linear-gradient(#ecebe8,#b0612d 55%,#e6e4e0)" role="img" aria-label="Staircase with timber treads"></div>
    <div class="btn" style="left:520px;top:2982px;width:160px;height:42px;font-size:12px">View All Gallery</div>
  </section>

  <section>
    <div class="abs" style="left:0;top:3383px;width:1200px;height:372px;background:var(--black)"></div>
    <svg class="abs" style="left:142px;top:3100px" width="916" height="402" viewBox="0 0 916 402">
      <path d="M0 172 Q0 150 25 140 L410 8 Q458 -8 506 8 L891 140 Q916 150 916 172 V402 H0 Z" fill="#ec1c24"/>
    </svg>
    <h2 class="section-title" style="top:3168px">Contact Us</h2>
    <div class="field" style="left:354px;top:3255px;width:241px;height:34px">Your Name*</div>
    <div class="field" style="left:605px;top:3255px;width:241px;height:34px">Email*</div>
    <div class="field" style="left:354px;top:3302px;width:241px;height:34px">Phone*</div>
    <div class="field" style="left:605px;top:3302px;width:241px;height:34px">Inquiry For*</div>
    <div class="field" style="left:354px;top:3350px;width:492px;height:58px">How can we help you?</div>
    <div class="btn" style="left:554px;top:3456px;width:92px;height:34px;background:var(--black)">Submit</div>
  </section>

  <footer>
    <nav class="footer-nav">
      <a style="left:434px;color:var(--red)">Home</a>
      <a style="left:513px">Services</a>
      <a style="left:607px">Gallery</a>
      <a style="left:694px">Contact Us</a>
    </nav>
    <div class="abs" style="left:142px;top:3562px;width:916px;height:1px;background:#444"></div>
    <div class="abs" style="left:155px;top:3602px;font-size:30px;font-weight:700;color:#fff">GLEAMSTONE</div>
    <div class="abs" style="left:155px;top:3646px;width:190px;text-align:center;font-size:13px;font-weight:600;color:#fff;letter-spacing:3px">WORKS</div>
    <div class="abs" style="left:387px;top:3603px;width:1px;height:72px;background:#444"></div>
    <div class="abs" style="left:631px;top:3603px;width:1px;height:72px;background:#444"></div>
    <div class="abs" style="left:812px;top:3603px;width:1px;height:72px;background:#444"></div>
    <svg class="abs" style="left:418px;top:3620px" width="16" height="18" viewBox="0 0 16 18"><path d="M8 17 C3 11 2 9 2 6.5 A6 6 0 0 1 14 6.5 C14 9 13 11 8 17Z" fill="none" stroke="#fff" stroke-width="1.4"/><circle cx="8" cy="6.5" r="2.2" fill="none" stroke="#fff" stroke-width="1.4"/></svg>
    <div class="info" style="left:444px">123 Lorem ipsume Dilor<br>Site 32311 Lorem ipsume</div>
    <svg class="abs" style="left:664px;top:3620px" width="17" height="17" viewBox="0 0 17 17"><path d="M4 1.5 L6.5 5 L5 7 Q7 11 10 12 L12 10.5 L15.5 13 L14 15.5 Q7 16 2 8 Q1 4 4 1.5Z" fill="none" stroke="#fff" stroke-width="1.3"/></svg>
    <div class="info" style="left:696px">Call :<br>123 456 7890</div>
    <svg class="abs" style="left:845px;top:3621px" width="19" height="14" viewBox="0 0 19 14"><rect x="1" y="1" width="17" height="12" rx="1.5" fill="none" stroke="#fff" stroke-width="1.3"/><path d="M1.5 2 L9.5 8 L17.5 2" fill="none" stroke="#fff" stroke-width="1.3"/></svg>
    <div class="info" style="left:878px">Email :<br>info@gleamstoneworks.com</div>
    <div class="abs" style="left:0;top:3718px;width:1200px;height:1px;background:#333"></div>
    <div class="abs" style="left:142px;top:3728px;font-size:12px;color:#fff">© 2024 Gleamstone Works Flooring Home Improvement. All Rights Reserved.</div>
    <div class="abs" style="left:975px;top:3728px;width:22px;height:22px;border-radius:50%;background:var(--red)"></div>
    <div class="abs" style="left:1005px;top:3728px;width:22px;height:22px;border-radius:50%;background:var(--red)"></div>
    <div class="abs" style="left:1035px;top:3728px;width:22px;height:22px;border-radius:50%;background:var(--red)"></div>
  </footer>

</div>
</body>
</html>
```